I am looking for business cards and letterhead

I want a high-level look for CEO's who want a concierge level leadership consultant and organization development strategist

This needs to go with my brand: simple, elegant, clean. Please improve on this design while using these fonts and colors

Here is my website: CorinneHalvers.com

```html
<!DOCTYPE html>
<html lang="en">
<head>
<meta charset="utf-8">
<title>Corinne Halvers – Business Card</title>
<link rel="stylesheet" href="https://fonts.googleapis.com/css2?family=Montserrat:wght@400;600;700&display=swap">
<style>
  :root {
    --page-bg: #e9e6e0;
    --card-white: #ffffff;
    --brand-blue: #1f56a8;
    --brand-slate: #4a4d57;
    --text-dark: #2b2b2b;
    --gold-light: #f1e2bb;
    --gold-mid: #e4cc92;
    --gold-deep: #cfb072;
    --ring-gold: #e2c98f;
  }
  * { box-sizing: border-box; margin: 0; padding: 0; }
  html, body {
    width: 916px; height: 1200px; overflow: hidden;
    background: var(--page-bg);
    font-family: "Montserrat", Arial, sans-serif;
  }
  .canvas { position: relative; width: 916px; height: 1200px; }

  .card {
    position: absolute; left: 73px; width: 772px; height: 460px;
    border-radius: 22px; overflow: hidden;
    box-shadow: 0 6px 18px rgba(0,0,0,0.25);
  }
  .card-front { top: 107px; background: var(--card-white); }
  .card-back { top: 640px; }

  .front-wave { position: absolute; inset: 0; width: 772px; height: 460px; }

  .brand-mark {
    position: absolute; left: 191px; top: 165px;
    width: 166px; height: 166px; border-radius: 50%;
    border: 3px solid var(--ring-gold);
    display: flex; align-items: center; justify-content: center;
    text-align: center;
    color: var(--brand-blue); font-weight: 600; font-size: 17px; line-height: 1.3;
  }

  .divider {
    position: absolute; left: 388px; top: 149px;
    width: 2px; height: 199px; background: var(--brand-blue);
  }

  .details { position: absolute; left: 420px; top: 146px; color: var(--text-dark); }
  .name { font-size: 29px; font-weight: 700; color: var(--brand-slate); line-height: 1; }
  .name .first { color: var(--brand-blue); }
  .role { font-size: 16px; margin-top: 8px; }
  .address { font-size: 16px; line-height: 22px; margin-top: 20px; }
  .contacts { list-style: none; margin-top: 18px; font-size: 16px; }
  .contacts li { display: flex; align-items: center; height: 26px; }
  .contacts svg { width: 16px; height: 16px; margin-right: 12px; flex: none; }

  .back-pattern {
    position: absolute; inset: 0;
    background: linear-gradient(120deg, #f4e6c2 0%, var(--gold-mid) 45%, var(--gold-deep) 100%);
  }
  .back-seal {
    position: absolute; left: 580px; top: 277px;
    width: 92px; height: 92px; border-radius: 50%;
    border: 3px solid #ffffff;
  }
</style>
</head>
<body>
<div class="canvas">

  <section class="card card-front">
    <svg class="front-wave" viewBox="0 0 772 460" aria-hidden="true">
      <defs>
        <linearGradient id="goldFill" x1="0" y1="0" x2="0" y2="1">
          <stop offset="0" stop-color="#f3e6c4"/>
          <stop offset="1" stop-color="#e3ca90"/>
        </linearGradient>
      </defs>
      <path d="M0,330 C180,300 360,400 540,428 C640,442 720,410 772,318 L772,460 L0,460 Z" fill="url(#goldFill)"/>
      <path d="M0,316 C200,282 380,390 570,420 C650,432 710,420 760,398 C708,428 650,445 570,438 C380,415 200,318 0,346 Z" fill="var(--brand-blue)"/>
      <path d="M420,360 C560,420 680,400 772,300 L772,318 C700,402 590,430 460,384 Z" fill="#ffffff" opacity="0.85"/>
    </svg>

    <div class="brand-mark">Corinne<br>Halvers</div>
    <div class="divider"></div>

    <div class="details">
      <h1 class="name"><span class="first">Evan</span> Marsh</h1>
      <p class="role">CEO</p>
      <p class="address">48 Alder Lane,<br>Brookfield, USA</p>
      <ul class="contacts">
        <li>
          <svg viewBox="0 0 16 16"><path d="M2 5 C2 3 4 2 8 2 C12 2 14 3 14 5 L11 6 L10 5 L6 5 L5 6 Z M4 7 H12 L13 13 H3 Z" fill="var(--ring-gold)"/></svg>
          (08) 9400 2187
        </li>
        <li>
          <svg viewBox="0 0 16 16"><rect x="1" y="3" width="14" height="10" fill="var(--ring-gold)"/><path d="M1 3 L8 9 L15 3" stroke="#fff" stroke-width="1.3" fill="none"/></svg>
          info@CorinneHalvers.com
        </li>
        <li>
          <svg viewBox="0 0 16 16"><circle cx="8" cy="8" r="7" fill="var(--ring-gold)"/><path d="M1 8 H15 M8 1 C5 5 5 11 8 15 M8 1 C11 5 11 11 8 15" stroke="#fff" stroke-width="1" fill="none"/></svg>
          www.CorinneHalvers.com
        </li>
      </ul>
    </div>
  </section>

  <section class="card card-back">
    <div class="back-pattern" role="img" aria-label="Gold background with a repeating grid of embossed circular brand emblems"></div>
    <div class="back-seal"></div>
  </section>

</div>
</body>
</html>
```